Business card design for a dynamic IT consulting company

We need a business card design for a young firm, specialized in the Telecommunications/Consulting industry. The name of the company is Brask and Partners Business Consulting Ltd. (Short name: Brask and Partnes)
Brask = solve read reverse, so we aim to be uncomplicated and solution-oriented. The small pipe in our logo is also related to the word solve. So we need a new business card design, which is simple, eye catching and something non traditional (I would probably prefer a square shaped design rather than a rectangle, but open for suggestions). Attached our logo.

Target Market(s)

Usually our customers are Tier1 Telecoms providers (Q-Linkra, Parnexo, etc) and their executives.

Industry/Entity Type

Business

Contact Information for Business Card

Name: Gergely Halmindo
Email: g.halmindo@braskpartnera.hu
Web: www.braskpartnera.hu
Mobile: +36 30 555 0192
Title: Managing Director

Optional:
Company name: Brask and Partners Ltd.
Address: 1047 Budapest, Ravaszi str. 17/B, Hungary

Font styles to use
Other font styles liked:
• helveticaneue_medium, Prime Regular are used now.

Colors

Designer to choose colors to be used in the design.

Requirements
Must have
• I would like to have a 2 sided design.
Nice to have
• I thought if we make the logo a bit bigger (without the company name), that could go to the back with the company name below. I though, if the pipe in the logo is somehow touchable on the business card, would be nice and unique.

```html
<!DOCTYPE html>
<html lang="en">
<head>
<meta charset="utf-8">
<title>Brask &amp; Partners – Business Card</title>
<link rel="stylesheet" href="https://fonts.googleapis.com/css2?family=Exo+2:wght@400;500&display=swap">
<style>
  :root {
    --ink: #5b5c5f;
    --band: #5b5c5f;
    --paper: #ffffff;
    --edge: #8a8a8a;
    --accent-blue: #1ea3dc;
  }
  html, body {
    margin: 0;
    padding: 0;
    width: 1200px;
    height: 686px;
    overflow: hidden;
    background: var(--paper);
  }
  .card {
    position: relative;
    width: 1200px;
    height: 686px;
    box-sizing: border-box;
    border: 1px solid var(--edge);
    background: var(--paper);
    font-family: "Exo 2", sans-serif;
    color: var(--ink);
    overflow: hidden;
  }
  .brand {
    position: absolute;
    left: 48px;
    top: 0;
    height: 244px;
    display: flex;
    align-items: center;
    gap: 28px;
  }
  .brand-square {
    width: 44px;
    height: 44px;
    background: var(--accent-blue);
    flex: none;
  }
  .brand-name {
    margin: 0;
    font-size: 92px;
    font-weight: 400;
    line-height: 1;
    white-space: nowrap;
    color: var(--ink);
  }
  .side-band {
    position: absolute;
    left: 0;
    top: 245px;
    width: 163px;
    height: 441px;
    background: var(--band);
  }
  .icon {
    position: absolute;
    left: 111px;
    width: 34px;
    height: 34px;
  }
  .icon-person { top: 267px; }
  .icon-phone  { top: 460px; }
  .icon-mail   { top: 508px; }
  .icon-pin    { top: 552px; }
  .line {
    position: absolute;
    left: 191px;
    margin: 0;
    white-space: nowrap;
    line-height: 1;
  }
  .person-name  { top: 264px; font-size: 42px; font-weight: 500; }
  .person-title { top: 320px; font-size: 30px; }
  .phone        { top: 457px; font-size: 31px; }
  .email        { top: 510px; font-size: 31px; }
  .company      { top: 558px; font-size: 31px; }
  .address      { top: 609px; font-size: 31px; }
</style>
</head>
<body>
<div class="card">
  <div class="brand">
    <span class="brand-square" aria-hidden="true"></span>
    <h1 class="brand-name">Brask &amp; Partners</h1>
  </div>

  <div class="side-band"></div>

  <svg class="icon icon-person" viewBox="0 0 34 34" aria-hidden="true">
    <circle cx="17" cy="17" r="16" fill="#fff"/>
    <circle cx="17" cy="13" r="5.5" fill="none" stroke="#5b5c5f" stroke-width="2"/>
    <path d="M8 27c1.5-5 5-7 9-7s7.5 2 9 7" fill="none" stroke="#5b5c5f" stroke-width="2"/>
  </svg>
  <svg class="icon icon-phone" viewBox="0 0 34 34" aria-hidden="true">
    <circle cx="17" cy="17" r="16" fill="#fff"/>
    <rect x="12" y="7" width="10" height="20" rx="2" fill="none" stroke="#5b5c5f" stroke-width="2"/>
    <line x1="15.5" y1="24" x2="18.5" y2="24" stroke="#5b5c5f" stroke-width="1.6"/>
  </svg>
  <svg class="icon icon-mail" viewBox="0 0 34 34" aria-hidden="true">
    <circle cx="17" cy="17" r="16" fill="#fff"/>
    <rect x="8.5" y="11.5" width="17" height="11" fill="none" stroke="#5b5c5f" stroke-width="1.8"/>
    <path d="M8.5 11.5l8.5 6.5 8.5-6.5M8.5 22.5l6-5M25.5 22.5l-6-5" fill="none" stroke="#5b5c5f" stroke-width="1.6"/>
  </svg>
  <svg class="icon icon-pin" viewBox="0 0 34 34" aria-hidden="true">
    <circle cx="17" cy="17" r="16" fill="#fff"/>
    <path d="M17 27c-4.5-5.5-7-9-7-12.5a7 7 0 0 1 14 0C24 18 21.5 21.5 17 27z" fill="#5b5c5f"/>
    <circle cx="17" cy="14.5" r="2.8" fill="#fff"/>
  </svg>

  <p class="line person-name">Gergely Halmindo</p>
  <p class="line person-title">Managing Director</p>
  <p class="line phone">+36 30 555 0192</p>
  <p class="line email">g.halmindo@braskpartnera.hu</p>
  <p class="line company">Brask and Partners Ltd.</p>
  <p class="line address">1047 Budapest, Ravaszi str. 17/B, Hungary</p>
</div>
</body>
</html>
```